Global Expert Network Firm needs business card design

We need business card design for a new company based in Seoul, South Korea called 'Corwell Insight Partners'. We recruit industry experts covering all countries and connect our client and recruited expert by phone, face-to-face meetings and etc. We are a global expert network firm that is focused on delivering high-quality experts to our clients throughout the world. Our clients include multinational corporations, global consulting firms, private equity firms, venture capital firms, asset management companies.
We have made new logo and please find attachment.(Please use new logo)
Target Market(s)
Global Consulting Firms, Investment Firms, Private Equity Firms, Venture Capital Firms.
Industry/Entity Type
Recruitment
Contact Information for Business Card
We need two Languages (English and Korean Version).
The front is Korean and the back is English version.
[The back] [English]
Company Name: Corwell Insight Partners, Inc.
CEO Name: Daniel Park
Address: #507, Hanbit Bldg, 82 Maebongsan-ro, Dobong-gu, Seoul, 01327, Korea
Tel. +82 2 718 4052
Fax. +82 2 864 1097
Mobile. +82 10 7264 8815
Email: daniel@corwellip.com
Web: www.corwellip.com
[The front] [Korean] => Described in same order as English version.
회사명: 코웰인사이트파트너스(주)
대표이사: 박도현
주소: 서울시 도봉구 매봉산로 82 한빛빌딩 507호
Tel. 02 718 4052
Fax. 02 864 1097
Mobile. 010 7264 8815
Web: www.corwellip.com
Look and feel
Each slider illustrates characteristics of the customer's brand and the style your logo design should communicate.

```html
<!DOCTYPE html>
<html lang="en">
<head>
<meta charset="utf-8">
<title>Corwell Insight Partners — Business Card</title>
<link rel="stylesheet" href="https://fonts.googleapis.com/css2?family=Montserrat:wght@700&family=Nanum+Myeongjo&family=Questrial&display=swap">
<style>
  :root {
    --navy: #1c2452;
    --white: #ffffff;
    --paper: #ffffff;
  }
  * { margin: 0; padding: 0; box-sizing: border-box; }
  html, body {
    width: 878px; height: 1200px; overflow: hidden;
    background: var(--paper);
  }
  .sheet { position: relative; width: 878px; height: 1200px; }
  .card {
    position: absolute; left: 0; width: 878px; height: 569px;
    background: var(--navy); color: var(--white);
    font-family: "Questrial", sans-serif;
  }
  .card--english { top: 0; }
  .card--korean { top: 631px; }
  .card > * { position: absolute; white-space: nowrap; line-height: 1; }

  .brand {
    left: 625px; top: 118px; width: 200px;
    display: flex; flex-direction: column; align-items: flex-start; gap: 16px;
  }
  .brand-mark { width: 40px; height: 40px; background: var(--white); }
  .brand-name { font-size: 17px; letter-spacing: 0.2px; }

  .person-name {
    left: 38px; top: 252px;
    font-family: "Montserrat", sans-serif; font-weight: 700; font-size: 34px;
  }
  .person-title { left: 38px; top: 300px; font-size: 26px; }

  .contact { left: 37px; font-size: 25px; }
  .address { top: 365px; line-height: 31px; }
  .phones { top: 437px; }
  .web { top: 474px; }
  .label { opacity: 0.75; }

  .card--korean .person-name {
    top: 244px;
    font-family: "Nanum Myeongjo", serif; font-weight: 400; font-size: 38px;
  }
  .card--korean .person-title {
    top: 296px;
    font-family: "Nanum Myeongjo", serif; font-size: 29px;
  }
  .card--korean .address { top: 395px; font-family: "Nanum Myeongjo", serif; font-size: 28px; }
  .card--korean .address .num { font-family: "Questrial", sans-serif; font-size: 26px; }
  .card--korean .phones { top: 438px; }
  .card--korean .web { top: 475px; }
</style>
</head>
<body>
<div class="sheet">
  <section class="card card--english">
    <div class="brand"><span class="brand-mark"></span><span class="brand-name">Corwell Insight Partners</span></div>
    <h1 class="person-name">Daniel Park</h1>
    <p class="person-title">CEO</p>
    <p class="contact address">#507, Hanbit Bldg, 82 Maebongsan-ro, Dobong-gu,<br>Seoul, 01327, Korea</p>
    <p class="contact phones"><span class="label">F</span> +82 2 864 1097 | <span class="label">T</span> +82 2 718 4052 | <span class="label">M</span> +82 10 7264 8815</p>
    <p class="contact web">daniel@corwellip.com | www.corwellip.com</p>
  </section>

  <section class="card card--korean" lang="ko">
    <div class="brand"><span class="brand-mark"></span><span class="brand-name">Corwell Insight Partners</span></div>
    <h1 class="person-name">박도현</h1>
    <p class="person-title">대표이사</p>
    <p class="contact address">서울시 도봉구 매봉산로 <span class="num">82</span> 한빛빌딩 <span class="num">507</span>호</p>
    <p class="contact phones"><span class="label">F</span> 02 864 1097 | <span class="label">T</span> 02 718 4052 | <span class="label">M</span> 010 7264 8815</p>
    <p class="contact web">daniel@corwellip.com | www.corwellip.com</p>
  </section>
</div>
</body>
</html>
```